Business and Discussion forum website

I have long been an admirer of a good and professional business forum. Http://lanternbazaar.com got my attention and i am looking for a similar website to it. Basically, my website is going to discuss business, politics, entertainment and social issues. The website should be youthful and captivating. Users should be able to post threads, comments on threads, like and dislike comments. The administrator of the website will be able to delete post/threads. Users should be able to add each other as friends and subsequently be able to message/inbox each other. These are the basic stuffs the website should possess.

Industry/Entity Type

Business

Coding

Coded - Design and coding required

```html
<!DOCTYPE html>
<html lang="en">
<head>
<meta charset="utf-8">
<title>Crestline Forum</title>
<link rel="stylesheet" href="https://fonts.googleapis.com/css2?family=Open+Sans:wght@400;600;700&family=PT+Sans:wght@400;700&display=swap">
<style>
:root{
  --navy:#000090;
  --royal:#1e50ff;
  --sky:#7aacdf;
  --ink:#111;
  --row-alt:#f4f4f4;
  --stats:#bfcbc5;
  --footer:#0d0d0d;
  --nav-text:#c8c8e8;
  --nav-active:#2ea3f2;
  --link-teal:#2c7a8a;
  --icon-grey:#a8a8a8;
}
*{box-sizing:border-box;margin:0;padding:0}
html,body{width:1200px;height:874px;overflow:hidden;background:#fff}
body{position:relative;font-family:"PT Sans",sans-serif;color:var(--ink)}
.abs{position:absolute}

.site-header{left:0;top:0;width:1200px;height:71px;background:var(--navy)}
.brand{left:134px;top:19px;font-family:"Open Sans",sans-serif;font-weight:700;font-size:24px;color:#fff;letter-spacing:1px;white-space:nowrap}
.main-nav{right:0;top:0;height:71px;display:flex;align-items:center;gap:24px;padding-right:120px;font-family:"Open Sans",sans-serif;font-weight:600;font-size:15px;letter-spacing:1px}
.main-nav a{color:var(--nav-text);text-decoration:none}
.main-nav a.active{color:var(--nav-active)}

.page-title{left:120px;top:118px;font-family:"Open Sans",sans-serif;font-size:30px;font-weight:400;color:#222}
.search-box{left:120px;top:179px;width:114px;height:24px;background:#f2f2f2;font-size:10px;color:#888;padding:6px 4px}
.search-btn{left:239px;top:185px;font-size:11px;font-weight:700}
.adv-search{left:124px;top:203px;font-size:13.5px;font-weight:700}
.guest-note{left:866px;top:176px;font-size:9.5px;line-height:11px;color:#222}
.login{left:990px;top:176px;font-size:14px;font-weight:700}
.avatar{left:1035px;top:176px;width:45px;height:44px}

.topics-bar{left:120px;top:229px;width:960px;height:34px;background:#000;color:#fff;font-size:11px;font-weight:700;padding:10px 13px}
.crumb{left:124px;top:265px;font-size:13.5px;font-weight:700}

.category{left:120px;top:281px;width:960px;height:61px;background:var(--navy);color:#fff}
.category .name{position:absolute;left:55px;top:9px;font-size:18px;font-weight:700}
.category .desc{position:absolute;left:55px;top:35px;font-size:10px;color:#c8c8ee}
.category .rss{position:absolute;right:8px;top:10px;font-size:13px;font-weight:700;color:#000}

.head-row{left:120px;width:960px;background:var(--royal);font-size:14px;font-weight:700;color:var(--ink)}
.head-row span{position:absolute}

.row{left:120px;width:960px;font-size:10px}
.row.alt{background:var(--row-alt)}
.row span,.row svg{position:absolute}
.row .title{font-size:14px;font-weight:700}
.row .sub{font-size:10px}

.band{left:120px;top:535px;width:960px;height:41px;background:var(--sky);font-size:14px;font-weight:700;text-align:center;line-height:41px}

.stats{left:120px;top:733px;width:960px;height:71px;background:var(--stats);font-size:10px;color:#111}
.stats span{position:absolute}
.stats b{font-weight:700}

.site-footer{left:0;top:825px;width:1200px;height:49px;background:var(--footer)}
.credit{left:120px;top:16px;font-family:"Open Sans",sans-serif;font-size:14px;color:#777}
.social{right:120px;top:15px;display:flex;gap:27px}
.social i{display:block;width:20px;height:20px;border-radius:50%;background:#666}
</style>
</head>
<body>

<header class="site-header abs">
  <div class="brand abs">CRESTLINE FORUM</div>
  <nav class="main-nav abs">
    <a class="active">Home</a><a>General</a><a>Entertainment</a><a>Science/Technology</a>
    <svg width="16" height="16" viewBox="0 0 16 16"><circle cx="9.5" cy="6.5" r="5" fill="none" stroke="#9fa3d6" stroke-width="1.4"/><line x1="6" y1="10" x2="1.5" y2="14.5" stroke="#9fa3d6" stroke-width="1.4"/></svg>
  </nav>
</header>

<h1 class="page-title abs">Forum</h1>

<div class="search-box abs">Search…</div>
<div class="search-btn abs">Search</div>
<div class="adv-search abs">Advanced Search</div>
<div class="guest-note abs">Please consider registering<br>Guest</div>
<div class="login abs">Log In</div>
<svg class="avatar abs" viewBox="0 0 45 44" role="img" aria-label="Guest avatar">
  <rect width="45" height="44" fill="#bdbdbd"/>
  <circle cx="22.5" cy="15" r="9" fill="#e6e6e6"/>
  <path d="M6 40c2-11 9-15 16.5-15S37 29 39 40z" fill="#2a4bbf"/>
  <text x="22.5" y="41" font-size="8" font-weight="700" fill="#fff" text-anchor="middle" font-family="PT Sans,sans-serif">GUEST</text>
</svg>

<div class="topics-bar abs">New / Updated Topics <svg width="10" height="7" viewBox="0 0 10 7"><path d="M0 0h10L5 6z" fill="#fff"/></svg></div>
<div class="crumb abs">Forum</div>

<section class="category abs">
  <svg style="position:absolute;left:13px;top:18px" width="30" height="20" viewBox="0 0 30 20"><rect x="0" y="4" width="16" height="10" fill="#3a3aa0"/><rect x="12" y="0" width="18" height="12" fill="#4848b0"/></svg>
  <span class="name">General</span>
  <span class="desc">General</span>
  <span class="rss">RSS</span>
</section>

<div class="head-row abs" style="top:342px;height:43px">
  <span style="left:56px;top:13px">Forum</span>
  <span style="left:526px;top:13px">Topics</span>
  <span style="left:607px;top:13px">Last Post</span>
</div>

<div class="row abs" style="top:385px;height:50px">
  <svg style="left:14px;top:13px" width="16" height="23" viewBox="0 0 16 23"><path d="M0 0h11l5 5v18H0z" fill="var(--icon-grey)"/></svg>
  <span class="title" style="left:56px;top:10px">Politics</span>
  <span class="sub" style="left:56px;top:31px">Politics Discussion Forum</span>
  <span style="left:543px;top:20px">2</span>
  <span class="title" style="left:607px;top:9px">test</span>
  <span style="left:607px;top:27px">4 hours ago <span style="position:static;font-size:13px">admin</span></span>
  <svg style="left:940px;top:19px" width="11" height="11" viewBox="0 0 11 11"><path d="M4.5 0h2v11h-2zM0 4.5h11v2H0z" fill="#111"/></svg>
</div>
<div class="row alt abs" style="top:435px;height:50px">
  <svg style="left:14px;top:13px" width="16" height="23" viewBox="0 0 16 23"><path d="M0 0h11l5 5v18H0z" fill="var(--icon-grey)"/></svg>
  <span class="title" style="left:56px;top:10px">Crime</span>
  <span class="sub" style="left:56px;top:31px">Crime</span>
  <span style="left:543px;top:20px">0</span>
  <span style="left:606px;top:20px">No Topics</span>
  <svg style="left:938px;top:17px" width="11" height="14" viewBox="0 0 11 14"><path d="M2.5 6V4a3 3 0 0 1 6 0v2" fill="none" stroke="#111" stroke-width="1.8"/><rect y="6" width="11" height="8" fill="#111"/></svg>
</div>
<div class="row abs" style="top:485px;height:50px">
  <svg style="left:14px;top:13px" width="16" height="23" viewBox="0 0 16 23"><path d="M0 0h11l5 5v18H0z" fill="var(--icon-grey)"/></svg>
  <span class="title" style="left:56px;top:10px">Romance</span>
  <span class="sub" style="left:56px;top:31px">Romance</span>
  <span style="left:543px;top:20px">0</span>
  <span style="left:606px;top:20px">No Topics</span>
  <svg style="left:938px;top:17px" width="11" height="14" viewBox="0 0 11 14"><path d="M2.5 6V4a3 3 0 0 1 6 0v2" fill="none" stroke="#111" stroke-width="1.8"/><rect y="6" width="11" height="8" fill="#111"/></svg>
</div>

<div class="band abs">Unread and recently updated topics</div>

<div class="head-row abs" style="top:576px;height:43px">
  <span style="left:6px;top:13px">Topic</span>
  <span style="left:355px;top:13px">Forum</span>
  <span style="left:703px;top:13px">Last Post</span>
</div>

<div class="row abs" style="top:619px;height:48px">
  <span style="left:6px;top:11px;font-size:13px">test</span>
  <span class="title" style="left:355px;top:11px">Politics</span>
  <svg style="left:705px;top:7px" width="16" height="13" viewBox="0 0 16 13"><rect x="0.8" y="0.8" width="10" height="7" fill="none" stroke="#111" stroke-width="1.5"/><rect x="6" y="5" width="9" height="6" fill="#111"/></svg>
  <span class="title" style="left:725px;top:4px">admin</span>
  <span style="left:725px;top:22px;color:var(--link-teal)">4 hours ago</span>
</div>
<div class="row alt abs" style="top:667px;height:39px">
  <span style="left:6px;top:11px;font-size:13px">My First Topic</span>
  <svg style="left:705px;top:7px" width="16" height="13" viewBox="0 0 16 13"><rect x="0.8" y="0.8" width="10" height="7" fill="none" stroke="#111" stroke-width="1.5"/><rect x="6" y="5" width="9" height="6" fill="#111"/></svg>
  <span class="title" style="left:725px;top:4px">admin</span>
  <span style="left:725px;top:22px;color:var(--link-teal)">13 hours ago</span>
</div>

<section class="stats abs">
  <span style="left:7px;top:4px"><b>Forum Timezone:</b> UTC 0</span>
  <span style="left:7px;top:27px"><b>Most Users Ever Online:</b> 3</span>
  <span style="left:7px;top:43px"><b>Currently Online:</b> <span style="position:static;font-size:13px">admin</span></span>
  <span style="left:7px;top:58px">1 Guest(s)</span>
  <span style="left:845px;top:5px;font-weight:700;font-size:11px;color:#4a7a5a">Show Stats</span>
  <span style="left:910px;top:5px;font-weight:700;font-size:14px">All RSS</span>
</section>

<footer class="site-footer abs">
  <div class="credit abs">Designed by Crestline Forum</div>
  <div class="social abs" aria-label="Social links"><i></i><i></i><i></i><i></i></div>
</footer>

</body>
</html>
```